Olvar business stationery
Purified water company
Simple
Rodrigo Lemus
Gerente General
Calle 38 con Avenida Tzabalché
entre 164 y 166
Colonia Vista de Orquídeas
Mérida, Yucatán
rlem@purificadoraolvar-mx.com
www.purificadoraolvar-mx.com
- The logo font is Quadranta
- We would like all stationary, including letterhead, envelopes, business card, presentation folder, compliment card and fax cover
- Color gradient of blue
Light blue C=50 M=1 Y=0 K=0
Blue C=92 M=63 Y=1 K=0
Stroke light blue C=27 M=0 Y=1 K=0
siempre contigo...
- Name and image should be integrated in the design of the stationary
- Designers can split the name (quadranta font) and the waterfall image to use as they like during their designs

```html
<!DOCTYPE html>
<html lang="es">
<head>
<meta charset="utf-8">
<title>Olvar business stationery</title>
<link rel="stylesheet" href="https://fonts.googleapis.com/css2?family=Open+Sans:ital,wght@0,400;0,600;1,400;1,700&family=Nunito:wght@600&display=swap">
<style>
  :root {
    --bg: #5c5f63;
    --card: #ffffff;
    --blue: #1f67b1;
    --light-blue: #6cc6ee;
    --stroke-blue: #b9e5f7;
    --ink: #7a7d80;
    --rule: #9a9da0;
  }
  * { box-sizing: border-box; margin: 0; padding: 0; }
  html, body { width: 1200px; height: 901px; overflow: hidden; }
  body {
    background: var(--bg);
    font-family: "Open Sans", Arial, sans-serif;
    position: relative;
  }
  .card {
    position: absolute;
    left: 250px;
    width: 700px;
    height: 400px;
    background: var(--card);
    overflow: hidden;
  }
  .card--back { top: 35px; }
  .card--front { top: 466px; }

  .brand {
    font-family: "Nunito", "Open Sans", sans-serif;
    font-weight: 600;
    color: var(--light-blue);
    letter-spacing: 1px;
  }

  /* back */
  .back__scene {
    position: absolute;
    right: 40px; top: 30px;
    width: 300px; height: 300px;
    border-radius: 50%;
    background: radial-gradient(circle at 50% 45%, #eef4f1 0%, #f4f7f6 55%, rgba(255,255,255,0) 72%);
  }
  .card--back .brand {
    position: absolute; left: 50px; top: 140px;
    font-size: 110px; line-height: 1;
  }
  .back__tagline {
    position: absolute; left: 54px; top: 255px;
    font-size: 40px; color: var(--blue);
    letter-spacing: 0.5px;
  }

  /* front */
  .card--front .brand {
    position: absolute; left: 40px; top: 56px;
    font-size: 74px; line-height: 1;
  }
  .person {
    position: absolute; right: 40px; top: 168px; text-align: right;
  }
  .person__name {
    font-style: italic; font-weight: 700; font-size: 20px; color: var(--blue);
  }
  .person__role { font-size: 14px; color: var(--ink); }
  .divider {
    position: absolute; left: 40px; right: 40px; top: 222px;
    border-top: 1px solid var(--rule);
  }
  .address {
    position: absolute; left: 40px; top: 236px;
    font-style: italic; font-size: 17px; line-height: 25px; color: var(--ink);
  }
  .contact {
    position: absolute; left: 380px; right: 40px; top: 236px;
    list-style: none; font-size: 15px; color: var(--ink);
  }
  .contact li {
    display: flex; align-items: center; gap: 10px;
    height: 28px; border-bottom: 1px solid #d6d8da;
  }
  .contact li:last-child { border-bottom: none; }
  .contact svg { width: 14px; height: 14px; flex: none; }
</style>
</head>
<body>
  <section class="card card--back" aria-label="Reverso de tarjeta">
    <div class="back__scene" role="img" aria-label="Ilustración tenue de cascada"></div>
    <div class="brand">Olvar</div>
    <p class="back__tagline">siempre contigo...</p>
  </section>

  <section class="card card--front" aria-label="Frente de tarjeta">
    <div class="brand">Olvar</div>
    <div class="person">
      <p class="person__name">Rodrigo Lemus</p>
      <p class="person__role">Gerente General</p>
    </div>
    <div class="divider"></div>
    <address class="address">
      Calle 38 con Avenida Tzabalché<br>
      entre 164 y 166<br>
      Colonia Vista de Orquídeas<br>
      Mérida, Yucatán
    </address>
    <ul class="contact">
      <li>
        <svg viewBox="0 0 14 14"><rect x="3" y="1" width="8" height="12" rx="1.5" fill="none" stroke="#7a7d80" stroke-width="1.4"/><circle cx="7" cy="10.5" r="0.9" fill="#7a7d80"/></svg>
        999-4172605
      </li>
      <li>
        <svg viewBox="0 0 14 14"><rect x="1" y="3" width="12" height="8" rx="1" fill="none" stroke="#7a7d80" stroke-width="1.4"/><path d="M1.5 3.5 7 8l5.5-4.5" fill="none" stroke="#7a7d80" stroke-width="1.2"/></svg>
        rlem@purificadoraolvar-mx.com
      </li>
      <li>
        <svg viewBox="0 0 14 14"><circle cx="7" cy="7" r="5.8" fill="none" stroke="#7a7d80" stroke-width="1.3"/><ellipse cx="7" cy="7" rx="2.5" ry="5.8" fill="none" stroke="#7a7d80" stroke-width="1"/><path d="M1.2 7h11.6" stroke="#7a7d80" stroke-width="1"/></svg>
        www.purificadoraolvar-mx.com
      </li>
    </ul>
  </section>
</body>
</html>
```